Business Card Design Project

I have had my current business card for 6years and it is time to upgrade my business card. I have uploaded my old card
I am a retail specialty shop designer and want something designer looking but professional.
Target Market(s)
30-60 year old people in retail businesses
Industry/Entity Type
Retail
Requirements
Must have
- The Maple Fitouts logo (but colour can and style can be altered)
My name, position and contact details as per my existing card attached .
Rowan Pellicott Director
m: 0418593417
rowan@maplefitouts-example.com.au
www.maplefitouts-example.com.au
t:02 95318274 f: 02 95318291
po box 871 fernbrook nsw 2917
Nice to have
- Use both sides of the card

```html
<!DOCTYPE html>
<html lang="en">
<head>
<meta charset="utf-8">
<title>Maple Fitouts — Business Card</title>
<link rel="stylesheet" href="https://fonts.googleapis.com/css2?family=Barlow:wght@300;400;600&display=swap">
<style>
  :root {
    --backdrop: #1b1b1b;
    --card-dark: #141414;
    --card-dark-mid: #3a3a3a;
    --card-light: #f4f4f4;
    --card-light-shade: #bdbdbd;
    --ink-dark: #1e1e1e;
    --ink-soft: #3c3c3c;
    --ink-light: #ffffff;
  }
  * { box-sizing: border-box; margin: 0; padding: 0; }
  html, body {
    width: 1200px;
    height: 890px;
    overflow: hidden;
    background: var(--backdrop);
    font-family: "Barlow", "Helvetica Neue", Arial, sans-serif;
  }
  .stage {
    position: relative;
    width: 1200px;
    height: 890px;
    display: flex;
    justify-content: center;
    align-items: center;
    gap: 60px;
  }
  .card {
    position: relative;
    width: 340px;
    height: 530px;
    border-radius: 22px;
    overflow: hidden;
  }

  /* Contact side */
  .card--contact {
    background: linear-gradient(160deg, var(--card-light) 0%, #e2e2e2 55%, var(--card-light-shade) 100%);
  }
  .card--contact .plan-area {
    position: absolute;
    inset: 0;
    background: linear-gradient(170deg, rgba(255,255,255,0) 0%, rgba(150,150,150,0.16) 45%, rgba(255,255,255,0) 90%);
  }
  .contact {
    position: absolute;
    left: 46px;
    bottom: 62px;
    color: var(--ink-dark);
    text-transform: uppercase;
    letter-spacing: 0.04em;
  }
  .contact__name {
    font-weight: 600;
    font-size: 15px;
    letter-spacing: 0.06em;
  }
  .contact__role {
    font-size: 9px;
    color: var(--ink-soft);
    margin-bottom: 20px;
  }
  .contact__line {
    font-size: 10.5px;
    line-height: 1.35;
    color: var(--ink-soft);
  }
  .contact__group { margin-bottom: 14px; }
  .contact__address {
    font-size: 11.5px;
    color: var(--ink-dark);
  }

  /* Brand side */
  .card--brand {
    background: linear-gradient(150deg, var(--card-dark) 0%, #262626 40%, var(--card-dark-mid) 75%, #555 100%);
  }
  .card--brand .plan-area {
    position: absolute;
    inset: 0;
    background:
      radial-gradient(ellipse at 55% 30%, rgba(255,255,255,0.16) 0%, rgba(255,255,255,0) 55%),
      linear-gradient(180deg, rgba(90,90,90,0.25) 0%, rgba(20,20,20,0.1) 100%);
  }
  .brand {
    position: absolute;
    left: 0;
    right: 0;
    top: 220px;
    text-align: center;
    color: var(--ink-light);
    font-weight: 300;
    font-size: 34px;
    letter-spacing: 0.14em;
    text-transform: uppercase;
    line-height: 1.05;
  }
</style>
</head>
<body>
  <main class="stage">
    <section class="card card--contact">
      <div class="plan-area" role="img" aria-label="Faint architectural floor plan in light grey"></div>
      <div class="contact">
        <p class="contact__name">Rowan Pellicott</p>
        <p class="contact__role">Director</p>
        <div class="contact__group">
          <p class="contact__line">rowan@maplefitouts-example.com.au</p>
          <p class="contact__line">www.maplefitouts-example.com.au</p>
        </div>
        <div class="contact__group">
          <p class="contact__line">M: 0418593417</p>
          <p class="contact__line">T: 02 95318274</p>
          <p class="contact__line">F: 02 95318291</p>
        </div>
        <p class="contact__address">PO Box 871 Fernbrook NSW 2917</p>
      </div>
    </section>

    <section class="card card--brand">
      <div class="plan-area" role="img" aria-label="Architectural floor plan drawn in fine grey lines on black"></div>
      <p class="brand">Maple<br>Fitouts</p>
    </section>
  </main>
</body>
</html>
```